Conference program advertisement

Our business www.clinicledger.com.au is a good sponsor of the conference program run by the Southern Pacific Guild of Perioperative Physicians (SPGPP) here in Western Australia.
We have been running the same ad for a while and so we could do with a fresh new presence.
We have a conference banner and other signage that we'll use at the trade show so we're not looking to rebrand. Just looking for a new ad.
Specification is full colour A4, high res PDF
(Because I'm using my phone to create this job, I cannot seem to upload the existing ad. I'll do do ASAP.)

Target Market(s)

Specialist doctors

Industry/Entity Type

Trade

Font styles to use
Sans Serif

Colors

Designer to choose colors to be used in the design.

Requirements
Must have
• A4
Existing logo and colour scheme

```html
<!DOCTYPE html>
<html lang="en">
<head>
<meta charset="utf-8">
<title>Clinic Ledger Services – Advertisement</title>
<link rel="stylesheet" href="https://fonts.googleapis.com/css2?family=Oswald:wght@500;600&family=Roboto:wght@400;700&family=Pathway+Gothic+One&display=swap">
<style>
  :root {
    --backdrop: #8a8a8a;
    --sheet-top: #ffffff;
    --sheet-bottom: #d9e2e8;
    --brand-red: #d3201f;
    --band-red: #d93a2b;
    --ink: #222428;
    --ink-soft: #3a3d42;
    --photo-light: #e9e6e2;
    --photo-mid: #b9c6d8;
    --photo-teal: #1f5e5c;
  }
  * { box-sizing: border-box; margin: 0; padding: 0; }
  html, body {
    width: 1200px; height: 900px; overflow: hidden;
    background: var(--backdrop);
  }
  .flyer {
    position: absolute; left: 303px; top: 30px;
    width: 594px; height: 840px;
    background: linear-gradient(180deg, var(--sheet-top) 40%, var(--sheet-bottom) 100%);
    box-shadow: 0 10px 30px rgba(0,0,0,0.25);
    overflow: hidden;
  }
  .flyer__art { position: absolute; inset: 0; width: 594px; height: 840px; }
  .headline {
    position: absolute; right: 34px; top: 362px; width: 540px;
    font-family: "Oswald", sans-serif; font-weight: 600;
    font-size: 44px; line-height: 1.05; letter-spacing: 0.5px;
    color: var(--brand-red); text-align: right; text-transform: uppercase;
  }
  .intro {
    position: absolute; left: 34px; top: 474px; width: 526px;
    font-family: "Roboto", sans-serif; font-size: 11.2px; line-height: 1.45;
    color: var(--ink); text-align: justify;
  }
  .address-band {
    position: absolute; left: 0; top: 582px; width: 594px; height: 36px;
    background: var(--band-red);
    font-family: "Roboto", sans-serif; font-weight: 700; font-size: 16.5px;
    color: #fff; line-height: 36px; padding-left: 34px; letter-spacing: 0.2px;
    white-space: nowrap;
  }
  .services {
    position: absolute; left: 34px; top: 640px; width: 526px;
    font-family: "Pathway Gothic One", sans-serif; font-size: 15.5px;
    line-height: 1.4; color: var(--ink-soft); text-transform: uppercase;
    letter-spacing: 0.3px;
  }
</style>
</head>
<body>
  <article class="flyer">
    <svg class="flyer__art" viewBox="0 0 594 840">
      <defs>
        <linearGradient id="photoTone" x1="0" y1="0" x2="1" y2="1">
          <stop offset="0" stop-color="var(--photo-light)"/>
          <stop offset="0.55" stop-color="var(--photo-mid)"/>
          <stop offset="1" stop-color="var(--photo-teal)"/>
        </linearGradient>
      </defs>
      <path role="img" aria-label="Photo: a clinician in scrubs taking notes on a clipboard beside a patient resting in a hospital bed"
            d="M0 0 H594 V338 C420 330 200 270 0 150 Z" fill="url(#photoTone)"/>
      <path d="M0 150 C200 270 420 330 594 338 V346 C420 342 200 292 0 176 Z" fill="var(--brand-red)"/>
    </svg>

    <h1 class="headline">Is administration eating<br>up your valuable time?</h1>

    <p class="intro">Admin can consume a large amount of time for doctors working in private practice. From generating accounts to chasing up bad debts, from sitting on hold with health funds, or trawling through remittance advices to getting accreditation papers and submitting provider number applications properly – we're sure you would prefer to focus on being a doctor rather than worrying about paperwork and piles of admin. Clinic Ledger Services is here to help – contact us today if you're ready to remove the burden of admin.</p>

    <div class="address-band">Level 2, Suite 12, 450 Harbour Road, East Perth, WA, 6004</div>

    <p class="services">Private billing | VMP billing | Practice management | Organise lists | Cover lists | Banking | Public Rebate and health fund | Registrations | Fee estimates and informed financial consent | Bill Pay and credit card payments | Electronic claiming to health funds | GST reporting | Hospital accreditations</p>
  </article>
</body>
</html>
```